Our Company name is Bluefinch Office Cleaning Services. We are a Toronto(GTA) company looking for a brochure that with Logo design that gives a description of what we do.

We are a company that specializes in cleaning and sanitizing office/ workplaces. Our Experience includes working with school boards and hospitals, and have 15 plus years experience. We are looking for a simple design that catches and explains to our customers what we offer with some pics, which you can provide.

if you have any questions please let us know.

thank you

Target Market(s)

We are focusing Businesses

Font styles to use
Serif

Colors

Designer to choose colors to be used in the design.

Requirements
Must have
• Must have our name/Logo, brief description of what we do. Contact numbers, (416)-284-7316/ (647)591-2637 email (bluefinchofficecleaningservices@mailtrove.com
• Pics which you can provide
Nice to have
• We trust your imagination on this

```html
<!DOCTYPE html>
<html lang="en">
<head>
<meta charset="utf-8">
<title>Bluefinch Office Cleaning Services – Tri-fold Brochure</title>
<link rel="stylesheet" href="https://fonts.googleapis.com/css2?family=Lora:ital,wght@0,600;1,600;1,700&family=Open+Sans:wght@400;600;700&display=swap">
<style>
  :root{
    --blue:#1f6fd1;
    --blue-deep:#1650b0;
    --blue-light:#3f92ea;
    --white:#ffffff;
    --ink:#2b3340;
    --backdrop:#e3e4e7;
  }
  *{box-sizing:border-box;margin:0;padding:0}
  html,body{width:1200px;height:2571px;overflow:hidden;background:var(--backdrop)}
  body{font-family:"Open Sans",Arial,sans-serif;color:var(--ink)}
  .spread{position:absolute;left:40px;width:1120px;height:794px;background:var(--white);box-shadow:0 6px 22px rgba(0,0,0,.18);overflow:hidden}
  .spread--outside{top:446px}
  .spread--inside{top:1330px}
  .spread svg.art{position:absolute;inset:0;width:1120px;height:794px}
  .abs{position:absolute}

  .brand-name{font-family:"Lora",Georgia,serif;font-weight:600;color:var(--blue);line-height:1.02;text-align:center}
  .brand-name--panel{left:373px;width:374px;top:50px;font-size:31px}
  .brand-name--cover{left:747px;width:373px;top:528px;font-size:40px;color:var(--white)}
  .brand-name--small{left:208px;top:504px;width:150px;font-size:20px;text-align:left}

  .contact-box{left:405px;width:310px;height:44px;border:2px solid var(--blue);border-radius:8px;display:flex;align-items:center;justify-content:center;font-size:13px;font-weight:600;color:var(--ink);white-space:nowrap}
  .contact-box--phone{top:202px}
  .contact-box--email{top:268px;font-size:11.4px}
  .contact-label{position:absolute;top:-11px;left:50%;transform:translateX(-50%);background:var(--blue);color:var(--white);font-size:11px;font-weight:600;padding:1px 26px;border-radius:10px;white-space:nowrap}

  .cover-call{left:780px;width:307px;top:700px;height:52px;border:2px solid var(--white);border-radius:8px;display:flex;align-items:center;justify-content:center;color:var(--white);font-weight:700;font-size:17px;white-space:nowrap}
  .cover-call .contact-label{background:var(--white);color:var(--blue);font-size:14px;font-weight:700;top:-14px;padding:2px 30px}

  .section-title{font-family:"Lora",Georgia,serif;font-style:italic;font-weight:700;color:var(--blue)}
  .badge-title{width:156px;text-align:center;font-size:27px}
  .badge-title--about{left:53px;top:374px}
  .badge-title--why{left:35px;top:513px}
  .services-title{left:52px;top:36px;font-size:46px}

  .body-copy{font-size:12.4px;line-height:17.4px;text-align:left}
  .body-copy--about{left:32px;top:506px;width:312px;color:var(--white)}
  .body-copy--why{left:32px;top:640px;width:312px;color:var(--ink)}

  .service-list{list-style:none;width:300px}
  .service-list li{display:flex;gap:10px;align-items:flex-start;color:var(--white);font-size:12.4px;line-height:16px;margin-bottom:13px}
  .service-list svg{flex:0 0 17px;width:17px;height:17px;margin-top:1px}
  .service-list--a{left:400px;top:296px}
  .service-list--b{left:400px;top:604px}
  .service-list--c{left:775px;top:336px}
  .service-list--c li{white-space:nowrap}
</style>
</head>
<body>

<section class="spread spread--outside">
  <svg class="art" viewBox="0 0 1120 794">
    <defs>
      <linearGradient id="bandBlue" x1="0" y1="0" x2="1" y2="1">
        <stop offset="0" stop-color="#2a7de0"/><stop offset="1" stop-color="#1650b0"/>
      </linearGradient>
      <linearGradient id="photoOffice" x1="0" y1="0" x2="1" y2="1">
        <stop offset="0" stop-color="#eef1f2"/><stop offset=".6" stop-color="#cfd8d4"/><stop offset="1" stop-color="#8fae95"/>
      </linearGradient>
      <linearGradient id="photoSupplies" x1="0" y1="0" x2="1" y2="1">
        <stop offset="0" stop-color="#4a5058"/><stop offset=".55" stop-color="#3b5fa8"/><stop offset="1" stop-color="#b8433a"/>
      </linearGradient>
      <linearGradient id="photoCrew" x1="0" y1="0" x2="1" y2="1">
        <stop offset="0" stop-color="#e9eef3"/><stop offset=".5" stop-color="#5b93d6"/><stop offset="1" stop-color="#2f3a4a"/>
      </linearGradient>
    </defs>
    <rect class="photo" x="0" y="0" width="373" height="370" fill="url(#photoOffice)" role="img" aria-label="Photo: cleaning crew mopping and tidying a bright office"/>
    <rect class="photo" x="747" y="0" width="373" height="470" fill="url(#photoSupplies)" role="img" aria-label="Photo: basket of cleaning supplies, spray bottles, gloves and sponges"/>
    <path class="band" d="M0 360 C220 300 480 300 700 360 C880 410 1000 470 1120 455 L1120 794 L0 794 Z" fill="url(#bandBlue)"/>
    <rect class="photo" x="373" y="400" width="374" height="394" fill="url(#photoCrew)" role="img" aria-label="Photo: two smiling cleaners in blue aprons holding a mop and bucket"/>
    <path d="M0 332 C220 272 480 272 700 332 C880 382 1000 442 1120 427" fill="none" stroke="var(--blue-light)" stroke-width="18"/>
    <path d="M0 352 C220 292 480 292 700 352 C880 402 1000 462 1120 447" fill="none" stroke="var(--white)" stroke-width="22"/>
    <path d="M373 412 C500 440 620 430 747 405" fill="none" stroke="var(--blue)" stroke-width="14"/>
    <path d="M747 500 C850 520 980 520 1120 480" fill="none" stroke="var(--white)" stroke-opacity=".35" stroke-width="6"/>
    <circle cx="131" cy="393" r="78" fill="var(--white)"/>
    <circle cx="131" cy="393" r="68" fill="none" stroke="var(--blue)" stroke-width="1.6" stroke-dasharray="4 4"/>
    <line x1="373" y1="0" x2="373" y2="794" stroke="#000" stroke-opacity=".06"/>
    <line x1="747" y1="0" x2="747" y2="794" stroke="#000" stroke-opacity=".06"/>
  </svg>

  <h2 class="abs section-title badge-title badge-title--about">About Us</h2>
  <p class="abs body-copy body-copy--about">Bluefinch Office Cleaning Services keeps workplaces across Toronto and the GTA clean, safe and ready for business. For more than 15 years our trained crews have cleaned and sanitized offices, schools and hospital spaces, working with school boards and healthcare teams who expect the highest standards. We follow proven disinfection routines, use professional equipment and choose products that are safe for people and surfaces. Whether you need nightly janitorial service, a deep clean before a big day or regular sanitizing of busy common areas, we build a schedule around your business hours so your staff return to a fresh, healthy space every morning.</p>

  <div class="abs brand-name brand-name--panel">Bluefinch<br>Office Cleaning<br>Services</div>
  <div class="abs contact-box contact-box--phone"><span class="contact-label">Call Us</span>(416)-284-7316 or (647)591-2637</div>
  <div class="abs contact-box contact-box--email"><span class="contact-label">Email Us</span>bluefinchofficecleaningservices@mailtrove.com</div>

  <div class="abs brand-name brand-name--cover">Bluefinch<br>Office Cleaning<br>Services</div>
  <div class="abs cover-call"><span class="contact-label">Call Us Today</span>(416)-284-7316/ (647)591-2637</div>
</section>

<section class="spread spread--inside">
  <svg class="art" viewBox="0 0 1120 794">
    <defs>
      <linearGradient id="bandBlue2" x1="0" y1="0" x2="1" y2="1">
        <stop offset="0" stop-color="#2a7de0"/><stop offset="1" stop-color="#1650b0"/>
      </linearGradient>
      <linearGradient id="photoTeam" x1="0" y1="0" x2="1" y2="0">
        <stop offset="0" stop-color="#dfe6ee"/><stop offset=".5" stop-color="#3d67a8"/><stop offset="1" stop-color="#a45a48"/>
      </linearGradient>
      <linearGradient id="photoDesk" x1="0" y1="0" x2="1" y2="1">
        <stop offset="0" stop-color="#f1f3f5"/><stop offset=".6" stop-color="#c9cfd6"/><stop offset="1" stop-color="#e2c24a"/>
      </linearGradient>
      <linearGradient id="photoFloor" x1="0" y1="0" x2="1" y2="1">
        <stop offset="0" stop-color="#4f6b4a"/><stop offset=".6" stop-color="#8e8a82"/><stop offset="1" stop-color="#c9c4ba"/>
      </linearGradient>
    </defs>
    <rect class="photo" x="373" y="0" width="747" height="290" fill="url(#photoTeam)" role="img" aria-label="Photo: team of cleaners in blue uniforms with mops and a vacuum"/>
    <path class="band" d="M0 195 C250 145 520 185 747 250 C900 290 1020 280 1120 250 L1120 794 L373 794 L373 520 L0 520 Z" fill="url(#bandBlue2)"/>
    <path d="M0 185 C250 135 520 175 747 240 C900 280 1020 270 1120 240" fill="none" stroke="var(--white)" stroke-width="14"/>
    <rect class="photo" x="0" y="228" width="373" height="286" fill="url(#photoDesk)" role="img" aria-label="Photo: cleaner in yellow gloves wiping an office desk"/>
    <rect class="photo" x="747" y="560" width="373" height="234" fill="url(#photoFloor)" role="img" aria-label="Photo: worker polishing an outdoor floor with a scrubbing machine"/>
    <path d="M0 505 C250 470 500 560 760 545 C920 535 1020 520 1120 525" fill="none" stroke="var(--white)" stroke-width="40"/>
    <path d="M373 580 C520 592 640 588 760 572 C920 560 1020 548 1120 552" fill="none" stroke="var(--blue-light)" stroke-width="8"/>
    <circle cx="113" cy="532" r="74" fill="var(--white)"/>
    <circle cx="113" cy="532" r="64" fill="none" stroke="var(--blue)" stroke-width="1.6" stroke-dasharray="4 4"/>
    <line x1="373" y1="0" x2="373" y2="794" stroke="#000" stroke-opacity=".06"/>
    <line x1="747" y1="0" x2="747" y2="794" stroke="#000" stroke-opacity=".06"/>
  </svg>

  <h2 class="abs section-title services-title">Our Services</h2>
  <h2 class="abs section-title badge-title badge-title--why">Why Us</h2>
  <div class="abs brand-name brand-name--small">Bluefinch<br>Office Cleaning<br>Services</div>
  <p class="abs body-copy body-copy--why">Our crews are trained, insured and background checked. With 15+ years serving school boards and hospitals, we know how to clean to strict health standards. You get a dedicated supervisor, flexible scheduling and consistent results, backed by clear communication and fair pricing.</p>

  <ul class="abs service-list service-list--a">
    <li><svg viewBox="0 0 17 17"><circle cx="8.5" cy="8.5" r="8.5" fill="#fff"/><path d="M4.6 8.8l2.7 2.6 5-5.3" fill="none" stroke="#1f6fd1" stroke-width="2"/></svg>Daily and nightly office cleaning tailored to your schedule</li>
    <li><svg viewBox="0 0 17 17"><circle cx="8.5" cy="8.5" r="8.5" fill="#fff"/><path d="M4.6 8.8l2.7 2.6 5-5.3" fill="none" stroke="#1f6fd1" stroke-width="2"/></svg>Disinfection and sanitizing of high touch surfaces</li>
    <li><svg viewBox="0 0 17 17"><circle cx="8.5" cy="8.5" r="8.5" fill="#fff"/><path d="M4.6 8.8l2.7 2.6 5-5.3" fill="none" stroke="#1f6fd1" stroke-width="2"/></svg>Washroom and kitchen cleaning with restocking of supplies</li>
    <li><svg viewBox="0 0 17 17"><circle cx="8.5" cy="8.5" r="8.5" fill="#fff"/><path d="M4.6 8.8l2.7 2.6 5-5.3" fill="none" stroke="#1f6fd1" stroke-width="2"/></svg>Floor care including mopping, vacuuming and machine scrubbing</li>
  </ul>
  <ul class="abs service-list service-list--b">
    <li><svg viewBox="0 0 17 17"><circle cx="8.5" cy="8.5" r="8.5" fill="#fff"/><path d="M4.6 8.8l2.7 2.6 5-5.3" fill="none" stroke="#1f6fd1" stroke-width="2"/></svg>Carpet and upholstery deep cleaning for busy spaces</li>
    <li><svg viewBox="0 0 17 17"><circle cx="8.5" cy="8.5" r="8.5" fill="#fff"/><path d="M4.6 8.8l2.7 2.6 5-5.3" fill="none" stroke="#1f6fd1" stroke-width="2"/></svg>Window, glass and partition cleaning inside the workplace</li>
    <li><svg viewBox="0 0 17 17"><circle cx="8.5" cy="8.5" r="8.5" fill="#fff"/><path d="M4.6 8.8l2.7 2.6 5-5.3" fill="none" stroke="#1f6fd1" stroke-width="2"/></svg>Waste removal, recycling and secure disposal of materials</li>
    <li><svg viewBox="0 0 17 17"><circle cx="8.5" cy="8.5" r="8.5" fill="#fff"/><path d="M4.6 8.8l2.7 2.6 5-5.3" fill="none" stroke="#1f6fd1" stroke-width="2"/></svg>Post construction and move in or move out cleaning</li>
  </ul>
  <ul class="abs service-list service-list--c">
    <li><svg viewBox="0 0 17 17"><circle cx="8.5" cy="8.5" r="8.5" fill="#fff"/><path d="M4.6 8.8l2.7 2.6 5-5.3" fill="none" stroke="#1f6fd1" stroke-width="2"/></svg>School cleaning for boards and campuses</li>
    <li><svg viewBox="0 0 17 17"><circle cx="8.5" cy="8.5" r="8.5" fill="#fff"/><path d="M4.6 8.8l2.7 2.6 5-5.3" fill="none" stroke="#1f6fd1" stroke-width="2"/></svg>Healthcare grade cleaning for clinics</li>
    <li><svg viewBox="0 0 17 17"><circle cx="8.5" cy="8.5" r="8.5" fill="#fff"/><path d="M4.6 8.8l2.7 2.6 5-5.3" fill="none" stroke="#1f6fd1" stroke-width="2"/></svg>Floor stripping, waxing and polishing</li>
    <li><svg viewBox="0 0 17 17"><circle cx="8.5" cy="8.5" r="8.5" fill="#fff"/><path d="M4.6 8.8l2.7 2.6 5-5.3" fill="none" stroke="#1f6fd1" stroke-width="2"/></svg>One time deep cleans across the GTA</li>
  </ul>
</section>

</body>
</html>
```